General Dental Office Business Card

I run a private general dental office in southern California, and would like a refresh/redesign of my business card. I focus on quality care rather than volume. The email address on the uploaded current card should be updated to: info@marbleshoredental.example. The current card's logo is a deboss, but I am open to other ideas. The logo can be refreshed, but it is something that's been with me since the beginning of the office, so I wouldn't want a drastic redesign.
Target Market(s)
Adults 18-99, whoever needs dental services
Industry/Entity Type
Healthcare/Dental
Contact Information for Business Card
Name, Address, Phone, email
Colors
Designer to choose colors to be used in the design.
Requirements
Must have
- Logo (Same as original one in the uploaded file), space on back for appointment time/date

```html
<!DOCTYPE html>
<html lang="en">
<head>
<meta charset="utf-8">
<title>Marble Shore Dental – Business Card</title>
<link href="https://fonts.googleapis.com/css2?family=Mulish:wght@300;400;600&display=swap" rel="stylesheet">
<style>
  :root {
    --canvas: #e6e7e9;
    --card: #ffffff;
    --card-shade: #eeeff0;
    --band-light: #7d7d82;
    --band-dark: #5c5c61;
    --accent: #7ccbe2;
    --accent-faint: #e3f1f5;
    --ink: #6b6b70;
    --rule: #8d8d90;
    --on-band: #ffffff;
  }
  * { box-sizing: border-box; margin: 0; padding: 0; }
  html, body { width: 1200px; height: 1200px; overflow: hidden; }
  body {
    background: var(--canvas);
    font-family: "Mulish", sans-serif;
    display: flex;
    flex-direction: column;
    align-items: center;
    justify-content: center;
    gap: 60px;
  }
  .card {
    position: relative;
    width: 840px;
    height: 480px;
    background: linear-gradient(135deg, var(--card) 0%, var(--card) 55%, var(--card-shade) 100%);
    box-shadow: 0 10px 30px rgba(0,0,0,0.18);
    overflow: hidden;
  }
  /* Front */
  .card-front .band { position: absolute; inset: 0; }
  .card-front .identity { position: absolute; left: 150px; top: 70px; }
  .card-front .doctor-name {
    font-weight: 400; font-size: 44px; color: var(--accent); letter-spacing: 0.5px;
  }
  .card-front .specialty {
    font-weight: 400; font-size: 22px; color: var(--ink); margin-top: 2px; margin-left: -10px;
  }
  .contact {
    position: absolute; left: 60px; top: 255px; color: var(--on-band);
    font-size: 20px; font-weight: 400; line-height: 1.45; list-style: none;
  }
  .contact li { display: flex; align-items: center; gap: 10px; }
  .contact .address { padding-left: 28px; }
  .contact svg { width: 18px; height: 18px; flex: none; }
  .brand {
    position: absolute; left: 560px; top: 230px; width: 250px; height: 250px;
    display: flex; align-items: center; justify-content: center; text-align: center;
  }
  .brand-name {
    position: relative; font-weight: 600; font-size: 22px; line-height: 1.2; color: var(--accent);
  }
  /* Back */
  .card-back .watermark { position: absolute; left: 300px; top: 130px; }
  .appointment { position: absolute; left: 110px; right: 110px; }
  .appointment .rule { border-top: 1.5px solid var(--rule); }
  .appointment .label {
    text-align: right; font-size: 22px; color: var(--ink); margin-top: 6px; padding-right: 20px;
  }
  .appointment.date { top: 150px; }
  .appointment.time { top: 290px; }
</style>
</head>
<body>

  <section class="card card-front">
    <svg class="band" width="840" height="480" viewBox="0 0 840 480">
      <defs>
        <linearGradient id="bandFill" x1="0" y1="0" x2="0" y2="1">
          <stop offset="0" stop-color="var(--band-light)"/>
          <stop offset="1" stop-color="var(--band-dark)"/>
        </linearGradient>
      </defs>
      <path d="M0 225 H600 A135 135 0 0 0 585 480 H0 Z" fill="url(#bandFill)"/>
      <circle cx="685" cy="355" r="138" fill="var(--card)"/>
      <circle cx="685" cy="355" r="118" fill="none" stroke="var(--accent)" stroke-width="10"/>
    </svg>

    <header class="identity">
      <h1 class="doctor-name">Evan J. Marlow DDS</h1>
      <p class="specialty">General Dentistry</p>
    </header>

    <ul class="contact">
      <li class="address">1280 Harbor View Parkway Coveport,<br>CA 90210</li>
      <li>
        <svg viewBox="0 0 24 24" aria-hidden="true"><path fill="currentColor" d="M6.6 10.8a15.1 15.1 0 0 0 6.6 6.6l2.2-2.2a1 1 0 0 1 1-.25 11.4 11.4 0 0 0 3.6.57 1 1 0 0 1 1 1V20a1 1 0 0 1-1 1A17 17 0 0 1 3 4a1 1 0 0 1 1-1h3.5a1 1 0 0 1 1 1c0 1.25.2 2.45.57 3.57a1 1 0 0 1-.25 1z"/></svg>
        555-014-2290
      </li>
      <li>
        <svg viewBox="0 0 24 24" aria-hidden="true"><path fill="currentColor" d="M3 5h18v14H3z M3 5l9 7 9-7" stroke="#6a6a6f" stroke-width="1.5"/></svg>
        info@marbleshoredental.example
      </li>
      <li>
        <svg viewBox="0 0 24 24" aria-hidden="true"><circle cx="12" cy="12" r="9" fill="currentColor"/><path d="M3 12h18M12 3v18" stroke="#6a6a6f" stroke-width="1.6"/></svg>
        www.marbleshoredental.example
      </li>
    </ul>

    <div class="brand">
      <span class="brand-name">Marble Shore<br>Dental</span>
    </div>
  </section>

  <section class="card card-back">
    <svg class="watermark" width="240" height="240" viewBox="0 0 240 240" aria-hidden="true">
      <circle cx="120" cy="120" r="120" fill="var(--accent-faint)"/>
    </svg>
    <div class="appointment date">
      <div class="rule"></div>
      <p class="label">Appointment Date</p>
    </div>
    <div class="appointment time">
      <div class="rule"></div>
      <p class="label">Time</p>
    </div>
  </section>

</body>
</html>
```